Marlo Tidy Yard Website

We need a website design for this new company. I've attached the company logo. This company is in the construction industry that provides general labor, maintenance and cleaning for construction sites. We want a clean and simple website that can be easy to navigate.

Target Market(s)

Construction industry

Industry/Entity Type

Construction

Number of Pages Required

2 page

Font styles to use
Sans Serif

```html
<!DOCTYPE html>
<html lang="en">
<head>
<meta charset="utf-8">
<title>Marlo Tidy Yard</title>
<link rel="stylesheet" href="https://fonts.googleapis.com/css2?family=Oswald:wght@400;500;600;700&family=Arimo:wght@400;700&display=swap">
<style>
:root{
  --navy:#14145a;
  --blue:#2b86f0;
  --orange:#ff7a12;
  --sky:#dce9f8;
  --pale:#e4eefa;
  --ink:#1c1c5e;
  --rule:#9fb7d8;
  --white:#ffffff;
}
*{margin:0;padding:0;box-sizing:border-box}
html,body{width:1200px;height:3000px;overflow:hidden;background:var(--white)}
body{position:relative;font-family:"Arimo",Arial,sans-serif;color:var(--ink)}
.abs{position:absolute}
.btn{position:absolute;display:flex;align-items:center;justify-content:center;gap:14px;background:var(--blue);color:var(--white);border-radius:16px;font-size:12px;height:32px}
.btn svg{width:14px;height:10px}
.tag{position:absolute;font-family:"Oswald",sans-serif;font-weight:500;letter-spacing:2px;font-size:16px;color:var(--navy)}
.rule{position:absolute;height:1px;background:var(--rule);width:160px}
.copy{position:absolute;font-size:11.5px;line-height:15px;color:var(--ink)}

/* hero */
.hero{left:0;top:0;width:1200px;height:638px;background:linear-gradient(180deg,#dfe8f2 0%,#4f6e93 14%,#1d3457 38%,#14243e 55%,#3b3640 66%,#1d3e6a 78%,#0e1f3c 100%)}
.topline{top:6px;font-size:11px;color:var(--navy);display:flex;align-items:center;gap:8px}
.toplinks{right:136px;top:12px;display:flex;gap:20px;font-family:"Oswald",sans-serif;font-size:10px;color:var(--navy);letter-spacing:.5px}
.mainnav{left:134px;top:56px;display:flex;gap:28px;font-family:"Oswald",sans-serif;font-size:11.5px;color:var(--navy);letter-spacing:.5px}
.brand{font-family:"Oswald",sans-serif;font-weight:700;color:var(--navy);text-transform:uppercase;line-height:1;text-align:center}
.hero .brand{left:520px;top:22px;width:160px;font-size:26px;line-height:26px}
.auth{position:absolute;height:20px;border-radius:3px;font-family:"Oswald",sans-serif;font-size:11px;color:var(--white);display:flex;align-items:center;justify-content:center;letter-spacing:1px}
.auth.up{background:var(--navy)}
.auth.in{background:var(--orange)}
.hero-title{left:0;width:1200px;top:222px;text-align:center;font-family:"Oswald",sans-serif;font-weight:500;font-size:142px;line-height:150px;color:var(--white);letter-spacing:2px}
.hero-sub{left:160px;width:880px;top:372px;text-align:center;font-size:21px;line-height:24px;color:#e8eef6}

/* blobs */
.blob svg{display:block;width:100%;height:100%}

/* cards */
.works{top:1328px;left:0;width:1200px;display:flex}
.work{width:300px;height:384px;border:1px solid #cfd8e4;position:relative}
.work .shot{height:330px}
.work .cap{height:54px;text-align:center;padding-top:14px;font-size:12px;color:var(--ink)}
.work .cap small{display:block;font-size:8px;color:#556;margin-top:3px}
.work.active .cap{background:var(--blue);color:var(--white)}
.work.active .cap small{color:#dfeaff}
.work.active .cap svg{position:absolute;right:28px;top:351px;width:14px;height:10px}

.video{left:134px;top:1962px;width:554px;height:336px;background:linear-gradient(160deg,#9cc3d6 0%,#3d7795 35%,#163a55 70%,#2a6f8c 100%);box-shadow:0 4px 10px rgba(0,0,0,.35)}
.video .label{position:absolute;left:20px;bottom:14px;color:var(--white);font-size:19px;letter-spacing:1px}
.play{position:absolute;left:250px;top:138px;width:58px;height:58px;border:2px solid var(--white);border-radius:50%}

.quote{left:460px;top:2548px;width:620px;text-align:center;font-size:11.5px;line-height:15px;color:var(--ink)}
.author{left:460px;top:2612px;width:620px;text-align:center;font-size:11.5px;line-height:14px;color:var(--navy)}
.pager{left:700px;top:2692px;display:flex}
.pager span{width:44px;height:24px;display:flex;align-items:center;justify-content:center;border:1px solid var(--blue)}
.pager span.on{background:var(--blue)}

/* footer */
.footer{left:0;top:2812px;width:1200px;height:188px;background:var(--sky)}
.footer .brand{left:140px;top:30px;font-size:26px;line-height:28px;text-align:left}
.social{left:136px;top:108px;display:flex;gap:12px}
.social i{display:block;width:12px;height:12px;border-radius:50%;background:var(--blue)}
.flinks{font-size:9.5px;line-height:17px;color:var(--blue);letter-spacing:.8px;text-transform:uppercase}
.fline{position:absolute;top:146px;height:1px;background:#9aaccc}
.legal{left:0;width:1200px;top:160px;text-align:center;font-size:8px;color:var(--blue)}
</style>
</head>
<body>

<!-- HERO -->
<header class="hero abs">
  <div class="abs" role="img" aria-label="Night city skyline with a tall tower reflected in the water" style="inset:0"></div>
  <div class="topline abs" style="left:134px">
    <svg width="12" height="12" viewBox="0 0 12 12"><path d="M3 1l2 2-1 2c1 1.5 2 2.5 3 3l2-1 2 2-2 2C5 10 2 7 1 3z" fill="var(--orange)"/></svg>
    <span>+00 0000 0001</span>
    <svg width="16" height="11" viewBox="0 0 16 11" style="margin-left:18px"><rect width="16" height="11" fill="var(--orange)"/><path d="M0 0l8 6 8-6" fill="none" stroke="#fff" stroke-width="1.2"/></svg>
    <span>info@marlotidy.com</span>
  </div>
  <nav class="toplinks abs"><span>FAQ</span><span>CONTACT US</span><span>DEMO</span></nav>
  <nav class="mainnav abs"><span>HOW IT WORKS</span><span>PRODUCTS</span><span>NEWS</span><span>ABOUT</span></nav>
  <div class="brand abs">Marlo<br>Tidy Yard</div>
  <div class="auth up" style="left:930px;top:48px;width:62px">SIGN UP</div>
  <div class="auth in" style="left:998px;top:48px;width:66px">SIGN IN</div>
  <h1 class="hero-title abs">WE INNOVATE</h1>
  <p class="hero-sub abs">We Focus On Innovations, As Perfect Technologies And Global Experience Make Us Innovators In The Construction Industry</p>
  <div class="btn" style="left:480px;top:460px;width:240px;height:56px;border-radius:28px;font-size:15px">View Projects
    <svg viewBox="0 0 14 10"><path d="M0 5h12M8 1l4 4-4 4" fill="none" stroke="#fff" stroke-width="1.8"/></svg></div>
</header>

<!-- ABOUT -->
<section>
  <div class="blob abs" style="left:40px;top:676px;width:480px;height:420px">
    <svg viewBox="0 0 480 420">
      <defs><linearGradient id="glassA" x1="0" y1="0" x2="1" y2="1"><stop offset="0" stop-color="#cfe2ea"/><stop offset=".45" stop-color="#3f7a8c"/><stop offset="1" stop-color="#0f2d3a"/></linearGradient></defs>
      <path d="M60 60C150-10 330 0 430 80c60 50 50 140 10 150C370 250 260 240 150 300 80 340 40 400 20 330-10 230-20 120 60 60z" fill="var(--pale)"/>
      <path role="img" aria-label="Glass office tower seen from below" d="M70 70C160 20 330 40 420 120c30 30 20 60-10 70-90 20-200 40-260 110-40 50-90 110-110 60C0 290 0 130 70 70z" fill="url(#glassA)"/>
    </svg>
  </div>
  <div class="tag" style="left:568px;top:730px">ABOUT US</div>
  <p class="abs" style="left:568px;top:758px;width:480px;font-size:20px;line-height:24px;color:var(--navy)">“Our mission is to provide the best home improvement experience, stress free.”</p>
  <div class="rule" style="left:568px;top:815px;width:164px"></div>
  <p class="copy" style="left:568px;top:850px;width:500px;font-size:10px;line-height:14.5px">We deliver an awesome experience for our homeowners ensuring the best results for all their home improvement needs. At all costs.<br>We set the standard of excellence in partnering, service, and product, for home improvement professionals.<br>We are passionate about our uncompromising commitment to WOW customer service.<br>We believe in connection. We listen, and ask to understand rather than to be understood.<br>We are a positive team and have a family spirit; caring for and challenging each other.<br>We always celebrate success.<br>We enjoy what we do and have fun.<br>We have an open mind, seeking different perspectives to always learn something new.<br>We genuinely care for our customers and each other.<br>We accept failure for what it is. It sucks. Don't bask in it; grow from it.</p>
  <div class="btn" style="left:570px;top:1036px;width:128px">Get Started
    <svg viewBox="0 0 14 10"><path d="M0 5h12M8 1l4 4-4 4" fill="none" stroke="#fff" stroke-width="1.8"/></svg></div>
</section>

<!-- WORK -->
<section>
  <div class="tag" style="left:136px;top:1180px">THE WORK WE HAVE DONE</div>
  <p class="copy" style="left:134px;top:1228px;width:640px">Construction Industry is one of the most booming industries in the whole world. This industry is mainly an urban based one which is concerned with preparation as well as construction of real estate properties. The repairing of any existing building or making certain alterations in the same also comes under Construction Industry. This industry can be categorized into three basic categories namely :-</p>
  <div class="rule" style="left:134px;top:1290px"></div>
  <div class="btn" style="left:896px;top:1230px;width:128px">More Work
    <svg viewBox="0 0 14 10"><path d="M0 5h12M8 1l4 4-4 4" fill="none" stroke="#fff" stroke-width="1.8"/></svg></div>

  <div class="works abs">
    <div class="work"><div class="shot" role="img" aria-label="Steel frame of an unfinished building interior" style="background:linear-gradient(180deg,#3a3130,#6b5a55 50%,#3c3b48)"></div>
      <div class="cap">Construction Industry<small>©Marlo Tidy Yard</small></div></div>
    <div class="work active"><div class="shot" role="img" aria-label="Power line pylon against a blue sky" style="background:linear-gradient(180deg,#5d93c9,#b8d6ef 60%,#7fa6cc)"></div>
      <div class="cap">Construction Industry<small>©Marlo Tidy Yard</small>
        <svg viewBox="0 0 14 10"><path d="M0 5h12M8 1l4 4-4 4" fill="none" stroke="#fff" stroke-width="1.8"/></svg></div></div>
    <div class="work"><div class="shot" role="img" aria-label="Worker in a yellow hard hat repairing machinery" style="background:linear-gradient(160deg,#4b4b50,#8a7b76 45%,#2f2f35)"></div>
      <div class="cap">Construction Industry<small>©Marlo Tidy Yard</small></div></div>
    <div class="work"><div class="shot" role="img" aria-label="Yellow bulldozer on a site under blue sky" style="background:linear-gradient(170deg,#79a9d8,#d1b45a 55%,#6c5a3e)"></div>
      <div class="cap">Construction Industry<small>©Marlo Tidy Yard</small></div></div>
  </div>
</section>

<!-- RESEARCH -->
<section>
  <div class="tag" style="left:134px;top:1802px">CONSTRUCTION INDUSTRY RESEARCH</div>
  <p class="copy" style="left:134px;top:1850px;width:630px">Industry research is a vital tool for the survival of an industry in today's competition dominated market. Industry research is required to be carried out in order to increase sale of goods or products. Research pertaining to any industry encompasses the various means by which a company can enhance sales and retain the consumers.</p>
  <div class="rule" style="left:134px;top:1910px"></div>
  <div class="btn" style="left:896px;top:1852px;width:128px">More Research
    <svg viewBox="0 0 14 10"><path d="M0 5h12M8 1l4 4-4 4" fill="none" stroke="#fff" stroke-width="1.8"/></svg></div>

  <div class="video abs" role="img" aria-label="Glass walkway interior of a modern building">
    <div class="play"><svg viewBox="0 0 58 58" width="54" height="54"><path d="M23 18l16 11-16 11z" fill="#fff"/></svg></div>
    <div class="label">Industry Research</div>
  </div>

  <div class="blob abs" style="left:728px;top:1952px;width:440px;height:340px">
    <svg viewBox="0 0 440 340">
      <defs><linearGradient id="glassB" x1="1" y1="0" x2="0" y2="1"><stop offset="0" stop-color="#b9a6e8"/><stop offset=".5" stop-color="#4b3c9a"/><stop offset="1" stop-color="#1b1f55"/></linearGradient></defs>
      <path d="M300 10c80-20 140 40 120 140-15 90-100 170-210 180C110 340 40 320 20 260 5 200 60 150 150 120 220 95 240 25 300 10z" fill="var(--pale)"/>
      <path role="img" aria-label="Purple glass skyscraper viewed from below" d="M310 40c60-10 110 40 95 120-15 80-90 140-190 150-80 8-150-10-170-60-10-30 40-50 110-70 80-25 90-130 155-140z" fill="url(#glassB)"/>
    </svg>
  </div>
</section>

<!-- TESTIMONIAL -->
<section>
  <div class="tag" style="left:134px;top:2384px">TESTIMONIAL</div>
  <h2 class="abs" style="left:134px;top:2426px;font-weight:400;font-size:24px;color:var(--navy)">What our customers says Somthing about us</h2>
  <div class="rule" style="left:134px;top:2490px"></div>
  <div class="btn" style="left:896px;top:2434px;width:128px">More Testimonial
    <svg viewBox="0 0 14 10"><path d="M0 5h12M8 1l4 4-4 4" fill="none" stroke="#fff" stroke-width="1.8"/></svg></div>

  <div class="blob abs" style="left:128px;top:2502px;width:240px;height:192px">
    <svg viewBox="0 0 240 192">
      <defs><linearGradient id="glassC" x1="0" y1="0" x2="1" y2="1"><stop offset="0" stop-color="#8a7ec0"/><stop offset=".5" stop-color="#3d2f6e"/><stop offset="1" stop-color="#1e1a40"/></linearGradient></defs>
      <path d="M40 20C100-10 200 0 225 50c20 40-10 70-60 80-40 8-60 50-110 60C20 196 0 160 5 110 10 70 10 35 40 20z" fill="var(--pale)"/>
      <path role="img" aria-label="Modern glass building at dusk" d="M45 30c60-20 140-5 160 40 10 25-20 40-60 50-40 10-60 50-100 60-30 6-40-20-38-60C10 80 20 40 45 30z" fill="url(#glassC)"/>
      <text x="52" y="130" font-family="Oswald, sans-serif" font-size="72" fill="#fff">“</text>
    </svg>
  </div>

  <p class="quote abs">“ I am proud of the thoughtfulness, commitment and quality of work Northline has demonstrated through the design, construction and commissioning of our production facility. Teamwork is critical to any project; the Harbor Roast and Northline teams worked well together to achieve a first-class production facility. ”</p>
  <p class="author abs">DANA WHITLOCK, VP OF MANUFACTURING, ENGINEERING AND QUALITY<br>HARBOR ROAST</p>
  <div class="pager abs">
    <span><svg width="14" height="10" viewBox="0 0 14 10"><path d="M14 5H2M6 1L2 5l4 4" fill="none" stroke="var(--blue)" stroke-width="1.8"/></svg></span>
    <span class="on"><svg width="14" height="10" viewBox="0 0 14 10"><path d="M0 5h12M8 1l4 4-4 4" fill="none" stroke="#fff" stroke-width="1.8"/></svg></span>
  </div>
</section>

<!-- FOOTER -->
<footer class="footer abs">
  <div class="brand abs">Marlo<br>Tidy Yard</div>
  <div class="social abs"><i></i><i></i><i></i></div>
  <ul class="flinks abs" style="left:394px;top:26px;list-style:none"><li>Home</li><li>About us</li><li>Results</li><li>Free info</li><li>Blog</li></ul>
  <ul class="flinks abs" style="left:520px;top:26px;list-style:none"><li>How it w</li><li>Products</li><li>News</li><li>FAQ</li><li>Contact us</li><li>Demo</li></ul>
  <div class="topline abs" style="left:830px;top:32px">
    <svg width="12" height="12" viewBox="0 0 12 12"><path d="M3 1l2 2-1 2c1 1.5 2 2.5 3 3l2-1 2 2-2 2C5 10 2 7 1 3z" fill="var(--orange)"/></svg>
    <span>+00 0000 0001</span>
    <svg width="16" height="11" viewBox="0 0 16 11" style="margin-left:18px"><rect width="16" height="11" fill="var(--orange)"/><path d="M0 0l8 6 8-6" fill="none" stroke="#fff" stroke-width="1.2"/></svg>
    <span>info@marlotidy.com</span>
  </div>
  <div class="auth up" style="left:930px;top:64px;width:62px">SIGN UP</div>
  <div class="auth in" style="left:998px;top:64px;width:66px">SIGN IN</div>
  <div class="fline" style="left:136px;width:258px"></div>
  <div class="fline" style="left:806px;width:258px"></div>
  <p class="legal abs">© Marlo Tidy Yard 2018 | All Rights Reserved</p>
</footer>

</body>
</html>
```